TEAL BEACON LICE REMOVAL labels

I need a label design for our MINT REPELLING SHAMPOO (LICE PREVENTION).
It also includes our MINT REPELLING CONDITIONER (LICE PREVENTION) and our MINT SPRAY (LICE PREVENTION) also includes LICE & NIT ELIMINATING MOUSSE (LICE TREATMENT) and a LICE ELIMINATOR 100% Dimethicone oil (LICE TREATMENT). The shampoo and conditioner are sulfate free, contains peppermint and other essential oils and is safe for the entire family. Label should be simple, modern and high end looking. Fun is good too if it looks nice!

Target Market(s)

Kids and Adults

Industry/Entity Type

Hair Care Product

Font styles to use
Sans Serif
Decorative

Requirements
Must have
• -Words that should be used: safe, non toxic, sulfate free, essential oils, pesticide free. - Naturally removes lice, super lice & nits are great words for the lice & nit eliminating mousse and treatment oil 100% Dimethicone oil
- On a side note there are no essential oils in the lice & nit eliminating mousse or treatment oil 100% Dimethicone oil
Nice to have
• Earth tone colors if possible
Kid safe, no fillers, colors or scents
100% effective (even against super lice)
8oz labels and 4oz labels
Should not have
• No pictures of lice

```html
<!DOCTYPE html>
<html lang="en">
<head>
<meta charset="utf-8">
<title>Teal Beacon Lice Removal – Mint Repelling Shampoo Label</title>
<link rel="stylesheet" href="https://fonts.googleapis.com/css2?family=Montserrat:wght@600&family=Noto+Serif:ital,wght@0,400;1,400;1,700&family=Work+Sans:wght@300;400;600&display=swap">
<style>
  :root {
    --teal: #31d8c3;
    --ink: #1b1b1b;
    --deep-teal: #123f3a;
    --frame: #6a2f8f;
    --white: #ffffff;
    --sans: "Work Sans", sans-serif;
    --display: "Montserrat", sans-serif;
    --serif: "Noto Serif", serif;
  }
  * { margin: 0; padding: 0; box-sizing: border-box; }
  html, body { width: 1200px; height: 480px; overflow: hidden; background: var(--white); }
  .stage { position: relative; width: 1200px; height: 480px; }
  .label {
    position: absolute; left: 296px; top: 9px;
    width: 1085px; height: 825px;
    transform: scale(0.56); transform-origin: 0 0;
    color: var(--ink);
  }
  .label > * { position: absolute; }
  .teal-band { left: 252px; top: 0; width: 456px; height: 825px; background: var(--teal); }
  .trim-frame { left: 20px; top: 20px; width: 1062px; height: 785px; border: 3px solid var(--frame); border-radius: 6px; }

  .brand-mark { display: flex; flex-direction: column; align-items: center; gap: 12px; text-align: center; }
  .brand-mark .dot { width: 70px; height: 70px; border-radius: 50%; border: 3px solid var(--ink); }
  .brand-mark .name { font-family: var(--sans); font-weight: 400; font-size: 20px; letter-spacing: 3px; line-height: 1.3; color: var(--ink); }
  .brand-mark--front { left: 55px; top: 80px; width: 210px; }
  .brand-mark--back { left: 885px; top: 520px; width: 180px; }
  .brand-mark--back .dot { width: 56px; height: 56px; }
  .brand-mark--back .name { font-size: 16px; letter-spacing: 2px; }

  .product-variant { left: 53px; top: 290px; font-family: var(--sans); font-weight: 300; font-size: 58px; line-height: 1; }
  .product-name { left: 53px; top: 345px; font-family: var(--sans); font-weight: 600; font-size: 56px; line-height: 1; }
  .tagline { left: 53px; top: 415px; font-family: var(--serif); font-style: italic; font-size: 26px; line-height: 1.15; }
  .tagline strong { font-weight: 700; display: block; }

  .oils-seal { left: 155px; top: 545px; width: 74px; height: 74px; border-radius: 50%; border: 3px solid var(--teal); }

  .claim-bar { height: 30px; background: var(--ink); color: var(--white); font-family: var(--serif); font-style: italic; display: flex; align-items: center; }
  .claim-bar--safe { left: 0; top: 630px; width: 252px; font-size: 24px; justify-content: flex-end; padding-right: 22px; }
  .claim-bar--kid { left: 427px; top: 630px; width: 303px; font-size: 16.5px; padding-left: 15px; }

  .free-from { left: 20px; top: 668px; width: 210px; text-align: right; font-family: var(--sans); font-weight: 300; font-size: 31px; line-height: 1; }
  .volume { left: 203px; top: 730px; font-family: var(--serif); font-style: italic; font-size: 42px; line-height: 1; }
  .volume small { font-size: 24px; }

  .category { left: 296px; top: 770px; transform: rotate(-90deg); transform-origin: 0 0; font-family: var(--display); font-weight: 600; font-size: 112px; letter-spacing: 2px; line-height: 1; color: var(--white); white-space: nowrap; }

  .promise { left: 440px; top: 78px; font-family: var(--serif); font-style: italic; font-size: 37px; line-height: 38px; color: var(--ink); }

  .effective { left: 440px; top: 668px; font-family: var(--sans); font-weight: 300; font-size: 33px; line-height: 1; color: var(--deep-teal); }
  .effective small { display: block; font-size: 13px; margin-top: 6px; }

  .info { left: 729px; top: 76px; width: 230px; }
  .info h3 { font-family: var(--serif); font-style: italic; font-weight: 400; font-size: 14px; margin: 6px 0 5px; }
  .info p { font-family: var(--sans); font-size: 11.5px; line-height: 14.2px; }

  .care-icons { left: 1018px; top: 235px; width: 34px; display: flex; flex-direction: column; gap: 14px; align-items: center; }

  .contact { left: 742px; top: 466px; font-family: var(--serif); font-style: italic; line-height: 1; }
  .contact strong { display: block; font-weight: 700; font-size: 38px; }
  .contact span { display: block; font-size: 24px; margin-top: 2px; }

  .brand-info { left: 850px; top: 677px; width: 199px; text-align: right; font-family: var(--sans); font-size: 14px; line-height: 14.3px; }
</style>
</head>
<body>
<main class="stage">
  <section class="label" aria-label="Mint Repelling Shampoo extended label">
    <div class="teal-band"></div>
    <div class="trim-frame"></div>

    <div class="brand-mark brand-mark--front">
      <span class="dot"></span>
      <span class="name">TEAL BEACON<br>LICE REMOVAL</span>
    </div>

    <h1 class="product-variant">Mint</h1>
    <h2 class="product-name">Repelling</h2>
    <p class="tagline"><strong>lice prevention</strong>for all family</p>

    <div class="oils-seal" role="img" aria-label="Essential oils seal"></div>

    <p class="claim-bar claim-bar--safe">safe - non toxic</p>
    <p class="free-from">sulfate &amp;<br>pesticide free</p>
    <p class="volume">8<small>fl oz</small></p>

    <p class="category">SHAMPOO</p>

    <p class="promise">with our<br>natural &amp;<br>soft<br>formulation<br>removes lice,<br>super lice<br>&amp; nits</p>

    <p class="claim-bar claim-bar--kid">Kid safe, no fillers, colors or scents</p>
    <p class="effective">100% effective<small>(even against super lice)</small></p>

    <div class="info">
      <h3>Directions</h3>
      <p>Wet hair thoroughly and apply a generous amount of shampoo. Massage into scalp and hair from roots to ends. Leave on for two minutes, then rinse well. Follow with conditioner. Use daily during lice season for best results.</p>
      <h3>Caution</h3>
      <p>For external use only. Avoid contact with eyes; if contact occurs, rinse with plenty of water. Discontinue use if irritation develops. Keep out of reach of children under two. Store in a cool, dry place away from direct sunlight.</p>
      <h3>Ingredients</h3>
      <p>Water, sodium cocoyl isethionate, cocamidopropyl betaine, glycerin, peppermint oil, rosemary oil, tea tree oil, spearmint oil, aloe vera leaf juice, panthenol, citric acid, sodium chloride, potassium sorbate, vitamin E.</p>
    </div>

    <div class="care-icons">
      <svg width="32" height="30" viewBox="0 0 32 30" role="img" aria-label="Recyclable">
        <path d="M16 3 L27 22 H5 Z" fill="none" stroke="#1b1b1b" stroke-width="3" stroke-linejoin="round"/>
      </svg>
      <svg width="32" height="32" viewBox="0 0 32 32" role="img" aria-label="Use within 18 months">
        <rect x="4" y="12" width="24" height="17" rx="3" fill="none" stroke="#1b1b1b" stroke-width="2"/>
        <line x1="4" y1="10" x2="24" y2="2" stroke="#1b1b1b" stroke-width="2"/>
        <text x="16" y="24" text-anchor="middle" font-family="Work Sans, sans-serif" font-size="8" fill="#1b1b1b">18m</text>
      </svg>
      <svg width="30" height="32" viewBox="0 0 30 32" role="img" aria-label="Dispose in bin">
        <circle cx="8" cy="5" r="3.5" fill="#1b1b1b"/>
        <rect x="14" y="12" width="13" height="18" fill="#1b1b1b"/>
        <rect x="5" y="11" width="6" height="19" fill="#1b1b1b"/>
      </svg>
    </div>

    <p class="contact"><strong>any question?</strong><span>please contact us</span></p>

    <div class="brand-mark brand-mark--back">
      <span class="dot"></span>
      <span class="name">TEAL BEACON<br>LICE REMOVAL</span>
    </div>

    <p class="brand-info">Brand Information<br>office adress<br>email adress<br>web site<br>social media</p>
  </section>
</main>
</body>
</html>
```